Card design for Heating and Cooling company

this is for a heating and cooling company we recently updated our logo and need to update our cards. We attached our logo so you can incorporate it into the card. We specialize in residential and commercial furnace and air condition repairs. Have been in business since 2014.

Phone number 555.284.9137

We need the following phrases
:Repairs, Installations, and maintenance
:Quality work at reasonable prices
:residential/commercial
:Licensed &Insured
:Email Pinegrovehvac47@mailbox-example.com
Name: Teodor K (Ted)
Also on back side I would like my logo with wording :Thank you for your business and refferal

Industry/Entity Type

Hvac

Contact Information for Business Card

:residential/commercial
:Licensed & Insured
Name: Teodor K (Ted)
Number:555.284.9136

Requirements
Must have
• Blue and red colors
Nice to have
• Maybe a pic of a furnace or air conditioner

```html
<!DOCTYPE html>
<html lang="en">
<head>
<meta charset="utf-8">
<title>Pinegrove Heating &amp; Cooling – Business Card</title>
<link href="https://fonts.googleapis.com/css2?family=Source+Sans+3:wght@400;600;700&display=swap" rel="stylesheet">
<style>
  :root{
    --bg:#2a2b2d;
    --red:#ff1a0a;
    --red-deep:#f0140c;
    --orange:#ff8a00;
    --yellow:#ffb800;
    --blue:#1a9be0;
    --ink:#1c1c1c;
    --white:#ffffff;
  }
  *{margin:0;padding:0;box-sizing:border-box}
  html,body{width:1200px;height:885px;overflow:hidden}
  body{
    background:var(--bg);
    font-family:"Source Sans 3",Arial,sans-serif;
    position:relative;
  }
  .card{
    position:absolute;
    left:285px;
    width:630px;
    height:360px;
    overflow:hidden;
    box-shadow:0 10px 30px rgba(0,0,0,.45);
  }
  /* back side */
  .card--back{
    top:52px;
    background:radial-gradient(ellipse 55% 70% at 50% 42%, var(--yellow) 0%, var(--orange) 35%, var(--red) 85%);
    color:var(--white);
    text-align:center;
  }
  .brand{
    display:flex;align-items:center;justify-content:center;gap:10px;
    font-weight:700;letter-spacing:1px;
  }
  .brand__dot{width:16px;height:16px;border-radius:50%;background:currentColor}
  .card--back .brand{margin-top:62px;font-size:30px;color:var(--white)}
  .services{margin-top:26px;font-size:17px;line-height:1.35;font-weight:400}
  .thanks{margin-top:34px;font-size:17px}
  /* front side */
  .card--front{
    top:472px;
    background:var(--white);
  }
  .card--front .brand{
    position:absolute;top:48px;right:40px;
    font-size:30px;color:var(--ink);
  }
  .contact{position:absolute;left:40px;top:166px}
  .contact__name{color:var(--blue);font-weight:700;font-size:25px}
  .contact__line{font-size:17px;color:#333;line-height:1.3}
  .contact__line b{color:var(--blue);font-weight:700}
  .band{position:absolute;left:0;top:0;width:630px;height:360px}
  .web{
    position:absolute;left:40px;bottom:26px;
    font-weight:700;font-size:17px;line-height:1;color:var(--ink);
  }
</style>
</head>
<body>

<section class="card card--back">
  <div class="brand"><span class="brand__dot"></span>PINEGROVE</div>
  <p class="services">Repairs, Installations, &amp; maintenance<br>
  Quality work at reasonable prices &bull; Residential/commercial<br>
  Licensed &amp; Insured</p>
  <p class="thanks">Thank you for your business &amp; refferal</p>
</section>

<section class="card card--front">
  <div class="brand"><span class="brand__dot"></span>PINEGROVE</div>

  <svg class="band" viewBox="0 0 630 360" aria-hidden="true">
    <defs>
      <linearGradient id="bandFill" x1="0" y1="0" x2="1" y2="0">
        <stop offset="0" stop-color="#ffffff"/>
        <stop offset="0.3" stop-color="#ffc640"/>
        <stop offset="0.6" stop-color="#ff8a00"/>
        <stop offset="1" stop-color="#ff2a0a"/>
      </linearGradient>
    </defs>
    <!-- sloped gradient wedge with a small notch tab -->
    <path d="M0 312 L492 246 L494 256 L508 254 L512 241 L630 225 L630 340 L0 340 Z" fill="url(#bandFill)"/>
    <rect x="0" y="338" width="630" height="22" fill="var(--red-deep)"/>
  </svg>

  <div class="contact">
    <div class="contact__name">Teodor K (Ted)</div>
    <div class="contact__line"><b>P:</b> 555.284.9136</div>
    <div class="contact__line"><b>E:</b> Pinegrovehvac47@mailbox-example.com</div>
  </div>
  <div class="web">www.Pinegrove-example.com</div>
</section>

</body>
</html>
```